Business Card Design Project

Black Writing

Torch Vell

Target Market(s)

18 - 80 year olds

Industry/Entity Type

Business

Requirements
Must have
• Clean

```html
<!DOCTYPE html>
<html lang="en">
<head>
<meta charset="utf-8">
<title>Torch Vell – Live Psychic Oracle Tarot Reading</title>
<link href="https://fonts.googleapis.com/css2?family=Questrial&display=swap" rel="stylesheet">
<style>
  :root {
    --gold: #a08a5a;
    --ink: #111111;
    --bg-edge: #e6e7e8;
    --bg-mid: #ffffff;
    --badge: #111111;
    --badge-ring: #b8964e;
  }
  html, body {
    margin: 0;
    padding: 0;
    width: 1200px;
    height: 741px;
    overflow: hidden;
  }
  .card {
    position: relative;
    width: 1200px;
    height: 741px;
    background: linear-gradient(180deg, var(--bg-edge) 0%, var(--bg-mid) 38%, var(--bg-mid) 55%, var(--bg-edge) 100%);
    font-family: "Questrial", "Century Gothic", sans-serif;
    color: var(--ink);
  }
  .line {
    position: absolute;
    left: 0;
    right: 0;
    margin: 0;
    text-align: center;
    white-space: nowrap;
    line-height: 1;
  }
  .title {
    top: 110px;
    font-size: 40px;
    color: var(--gold);
    font-weight: 400;
  }
  .services {
    top: 202px;
    font-size: 32px;
  }
  .phone {
    font-size: 26px;
  }
  .phone-card { top: 287px; }
  .phone-account { top: 327px; }
  .hours {
    font-size: 32px;
    color: var(--gold);
  }
  .hours-days { top: 398px; }
  .hours-times { top: 441px; }
  .conditions {
    position: absolute;
    top: 525px;
    right: 302px;
    margin: 0;
    font-size: 20.5px;
    line-height: 1;
    white-space: nowrap;
  }
  .badge {
    position: absolute;
    left: 912px;
    top: 442px;
    width: 220px;
    height: 220px;
  }
  .badge-name {
    font-family: "Questrial", "Century Gothic", sans-serif;
    font-size: 30px;
    fill: var(--gold);
  }
</style>
</head>
<body>
  <main class="card">
    <h1 class="line title">Live Psychic Oracle Tarot Reading</h1>
    <p class="line services">Romance, Sole Mates, Careers, Success – Oracle Tarot Reading</p>
    <p class="line phone phone-card">1300 555 218 (Credit / Debit Card)</p>
    <p class="line phone phone-account">1902 555 407 (Charged to the caller’s phone account)</p>
    <p class="line hours hours-days">Open: Monday – Friday</p>
    <p class="line hours hours-times">Times: 5pm – 10pm</p>
    <p class="conditions">*Conditions, fees and charges apply per minute</p>
    <svg class="badge" viewBox="0 0 220 220" aria-label="Torch Vell">
      <circle cx="110" cy="110" r="104" fill="var(--badge)" stroke="var(--badge-ring)" stroke-width="8"/>
      <text class="badge-name" x="110" y="120" text-anchor="middle">Torch Vell</text>
    </svg>
  </main>
</body>
</html>
```